Website for an electrical contractor :)

We are after a web site which can show pictures of our jobs and our capability in a professional, creative and easily understood way.

----- Brightmoor Electrical ------

We really want a visually good looking website with three sections

Section one:
'Completed projects'
We have a few pictures of jobs which we've completed and would like to show off with a brief description. (see uploads)

Section two:
'Our capabilities'
Just a list of what services we offer

Section three:
We would like a 'contact us' section which people can send us a short msg and upload a file for plans to be able to send to us. We would need their name, phone number and email details. We would also need a short privacy policy saying 'we do not disclose information to third parties'.
We also want to display our contact number and postal address

Good luck :)

Target Market(s)

Adults 25 years+
Business owners
Builders
Real estate agents

Industry/Entity Type

Electrical

Colors

Designer to choose colors to be used in the design.

Requirements
Must have
• Visually appealing
Easy to understand
In the 'Completed projects' section, must have a list for each project we do i can upload pictures for it.

```html
<!DOCTYPE html>
<html lang="en">
<head>
<meta charset="utf-8">
<title>Brightmoor Electrical</title>
<link rel="stylesheet" href="https://fonts.googleapis.com/css2?family=Dosis:wght@400;500&family=Open+Sans:wght@400;600&display=swap">
<style>
:root{
  --red:#e0343a;
  --red-deep:#c9262d;
  --red-soft:#d9444a;
  --ink:#1b1b1b;
  --grey:#a9a9a9;
  --white:#ffffff;
  --footer:#1f2020;
  --button:#6e4b4f;
}
*{margin:0;padding:0;box-sizing:border-box}
html,body{width:884px;height:1200px;overflow:hidden;background:var(--white)}
body{position:relative;font-family:"Open Sans",sans-serif;color:var(--ink)}
.abs{position:absolute}

/* header */
.site-header{position:absolute;left:0;top:0;width:884px;height:52px;background:var(--white)}
.brand{position:absolute;left:152px;top:7px;display:flex;align-items:center;gap:8px}
.brand-dot{width:14px;height:14px;border-radius:50%;background:var(--red)}
.brand-name{font-family:"Dosis",sans-serif;font-size:30px;font-weight:500;color:#555;line-height:36px}
.main-nav{position:absolute;top:0;left:490px;height:52px;display:flex}
.main-nav a{display:block;height:52px;line-height:50px;font-size:12px;color:#333;text-decoration:none;padding:0 10px;border-right:1px solid #e6e6e6}
.main-nav a:first-child{padding:0 13px 0 13px;line-height:50px;margin-top:-2px}
.main-nav a:last-child{border-right:none}

/* hero */
.hero{position:absolute;left:0;top:52px;width:884px;height:324px;overflow:hidden}
.hero-photo{position:absolute;inset:0;background:linear-gradient(160deg,#c93238 0%,#e0464b 40%,#cf3338 70%,#b8242b 100%)}
.hero-title{position:absolute;left:0;width:884px;text-align:center;font-family:"Dosis",sans-serif;color:var(--white);font-weight:400;letter-spacing:1.5px}
.hero-title.line-one{top:88px;font-size:44px;word-spacing:6px;left:12px}
.hero-rule{position:absolute;left:246px;top:141px;width:416px;height:1px;background:rgba(255,255,255,.85)}
.hero-title.line-two{top:145px;font-size:44px;left:12px}
.quote-button{position:absolute;left:355px;top:239px;width:175px;height:47px;background:var(--button);border:1px solid rgba(255,255,255,.75);color:var(--white);font-family:"Dosis",sans-serif;font-size:16px;text-align:center;line-height:45px;letter-spacing:.5px}

.notch{position:absolute;width:0;height:0;border-left:15px solid transparent;border-right:15px solid transparent;border-bottom:15px solid var(--white)}

/* split headings */
.split-heading{position:absolute;left:0;width:884px;height:96px}
.split-heading .left-word,.split-heading .right-word{position:absolute;font-family:"Dosis",sans-serif;font-size:26px;line-height:30px}
.mark-circle{position:absolute;left:411px;width:62px;height:62px;border-radius:50%;background:var(--grey);opacity:.75}
.accent{color:var(--red)}

/* projects */
.project-tile{position:absolute;top:499px;height:265px}
.project-tile.ongoing{left:0;width:441px;background:linear-gradient(180deg,#8e8e8c 0%,#d9d6cf 45%,#bdb9b2 75%,#55565a 100%)}
.project-tile.completed{left:442px;width:442px;background:linear-gradient(180deg,#3d7fd0 0%,#7eaee6 38%,#b3a88f 55%,#5f5d58 78%,#4a4a46 100%)}
.tile-label{position:absolute;background:var(--red);color:var(--white);font-family:"Dosis",sans-serif;font-size:26px;height:32px;line-height:32px;padding:0 6px;letter-spacing:.5px}

/* services band */
.services-band{position:absolute;left:0;top:860px;width:884px;height:176px;background:linear-gradient(180deg,#e0383e,#d93137 60%,#de3a40)}
.service-item{position:absolute;font-family:"Dosis",sans-serif;font-size:13px;color:var(--white);padding-left:10px}
.service-item::before{content:"";position:absolute;left:0;top:6px;width:5px;height:5px;border-radius:50%;background:var(--white)}
.services-intro{position:absolute;left:502px;top:798px;font-size:11.5px;line-height:16px;color:var(--red)}

/* social */
.social-row{position:absolute;left:382px;top:1051px;display:flex;gap:5px}
.social-row span{width:26px;height:26px;border-radius:50%;background:var(--red-soft)}

/* footer */
.site-footer{position:absolute;left:0;top:1089px;width:884px;height:111px;background:var(--footer);color:var(--white)}
.contact-item{position:absolute;top:30px;display:flex;align-items:center;gap:5px;font-family:"Cabin","Open Sans",sans-serif;font-size:11.5px}
.contact-item svg{fill:var(--white)}
.legal{position:absolute;left:0;width:884px;text-align:center;font-size:8px;color:#e8e8e8}
</style>
</head>
<body>

<header class="site-header">
  <div class="brand"><span class="brand-dot"></span><span class="brand-name">Brightmoor</span></div>
  <nav class="main-nav">
    <a href="#">Home</a>
    <a href="#">About us</a>
    <a href="#">Our services</a>
    <a href="#">Contact us</a>
  </nav>
</header>

<section class="hero">
  <div class="hero-photo" role="img" aria-label="Completed residential units and paved driveway under a red overlay"></div>
  <h1 class="hero-title line-one">BRIGHTMOOR ELECTRICAL</h1>
  <div class="hero-rule"></div>
  <p class="hero-title line-two">COMMUNICATIONS</p>
  <a class="quote-button">GET A QUOTE</a>
</section>
<div class="notch" style="left:427px;top:361px"></div>

<section class="split-heading" style="top:376px">
  <h2 class="left-word accent" style="left:252px;top:46px">Commercial</h2>
  <span class="mark-circle" style="top:28px"></span>
  <h2 class="right-word" style="left:509px;top:48px">Residential</h2>
</section>

<section class="projects">
  <div class="project-tile ongoing" role="img" aria-label="Lit commercial lounge room with leather armchairs and downlights"></div>
  <div class="project-tile completed" role="img" aria-label="Completed brick residential units with a paved courtyard under blue sky"></div>
  <span class="tile-label" style="left:133px;top:616px">ONGOING PROJECTS</span>
  <span class="tile-label" style="left:576px;top:616px">COMPLETED</span>
</section>
<div class="notch" style="left:427px;top:749px"></div>

<section class="split-heading" style="top:764px">
  <h2 class="left-word" style="left:257px;top:33px"><span class="accent">Our</span> Services</h2>
  <span class="mark-circle" style="top:17px"></span>
</section>
<p class="services-intro">Lorem ipsum dolor sit amet,<br>consectetuer adipiscing elit,</p>

<section class="services-band" role="img" aria-label="Building site with scaffolding under a red overlay"></section>
<ul class="services-list" style="list-style:none">
  <li class="service-item" style="left:143px;top:913px">24hr Support / faults</li>
  <li class="service-item" style="left:375px;top:913px">Temporary lighting</li>
  <li class="service-item" style="left:596px;top:913px">Energy efficient lighting</li>
  <li class="service-item" style="left:143px;top:964px">Commercial lighting</li>
  <li class="service-item" style="left:375px;top:964px">Led strip lighting</li>
  <li class="service-item" style="left:596px;top:964px">Illuminated signage</li>
</ul>
<div class="notch" style="left:427px;top:1021px"></div>

<div class="social-row"><span></span><span></span><span></span><span></span></div>

<footer class="site-footer">
  <div class="contact-item" style="left:153px">
    <svg width="10" height="11" viewBox="0 0 24 24"><path d="M6.6 10.8a15.1 15.1 0 0 0 6.6 6.6l2.2-2.2a1 1 0 0 1 1-.25 11.4 11.4 0 0 0 3.6.57 1 1 0 0 1 1 1V20a1 1 0 0 1-1 1A17 17 0 0 1 3 4a1 1 0 0 1 1-1h3.5a1 1 0 0 1 1 1c0 1.25.2 2.45.57 3.57a1 1 0 0 1-.25 1z"/></svg>
    <span>0400 123 456</span>
  </div>
  <div class="contact-item" style="left:272px">
    <svg width="8" height="12" viewBox="0 0 8 12"><path d="M1 0h6a1 1 0 0 1 1 1v10a1 1 0 0 1-1 1H1a1 1 0 0 1-1-1V1a1 1 0 0 1 1-1zm.3 1.3v8.4h5.4V1.3z"/></svg>
    <span>08 9000 1234</span>
  </div>
  <div class="contact-item" style="left:384px">
    <svg width="12" height="9" viewBox="0 0 12 9"><path d="M0 0h12v9H0zm1 1v.4l5 3.3 5-3.3V1zm0 1.6V8h10V2.6L6 5.9z"/></svg>
    <span>info@brightmoorelectrical.com.au</span>
  </div>
  <div class="contact-item" style="left:575px">
    <svg width="9" height="12" viewBox="0 0 9 12"><path d="M4.5 0A4.5 4.5 0 0 0 0 4.5C0 8 4.5 12 4.5 12S9 8 9 4.5A4.5 4.5 0 0 0 4.5 0zm0 6.3a1.8 1.8 0 1 1 0-3.6 1.8 1.8 0 0 1 0 3.6z"/></svg>
    <span>P.O Box 118 Harbour Vale W.A 6099</span>
  </div>
  <p class="legal" style="top:76px">we do not disclose information to third partie'</p>
  <p class="legal" style="top:89px">copyright © 2015 Brightmoor.com</p>
</footer>

</body>
</html>
```